Tarrow Building Ventures needs a Business card design and logo

We Need a business card design and logo for a Building & Construction business based in Melbourne. We work in both the Domestic & Commercial sector. We specialize in all aspects of building including extensions, Renovations, and alterations. Construction Management, Project Management, And labour hire
Updates

Industry/Entity Type

Business

```html
<!DOCTYPE html>
<html lang="en">
<head>
<meta charset="utf-8">
<title>Tarrow Building Ventures – Business Card</title>
<link href="https://fonts.googleapis.com/css2?family=Cinzel:wght@600&family=Orbitron:wght@500&display=swap" rel="stylesheet">
<style>
  :root {
    --backdrop: #d9dadb;
    --card: #ffffff;
    --green-dark: #1e9a3a;
    --green-light: #7cc142;
    --ink: #1a1a1a;
    --logo-ink: #3e4a44;
    --mark: #3aa845;
  }
  * { margin: 0; padding: 0; box-sizing: border-box; }
  html, body { width: 1200px; height: 771px; overflow: hidden; background: var(--backdrop); }
  .canvas { position: relative; width: 1200px; height: 771px; }

  .card {
    position: absolute;
    width: 540px; height: 309px;
    background: var(--card);
    box-shadow: 0 6px 18px rgba(0,0,0,.18);
    overflow: hidden;
  }
  .card--front { left: 45px; top: 231px; }
  .card--back  { left: 615px; top: 231px; }

  .brand {
    display: flex; align-items: center; gap: 10px;
    font-family: "Cinzel", serif; font-weight: 600;
    color: var(--logo-ink);
    white-space: nowrap;
  }
  .brand__dot { width: 14px; height: 14px; background: var(--mark); flex: none; }
  .card--front .brand { position: absolute; left: 50%; top: 50%; transform: translate(-50%,-50%); font-size: 24px; }
  .card--back .brand { position: absolute; right: 30px; top: 46px; font-size: 19px; }

  .band { position: absolute; inset: 0; }

  .contact {
    position: absolute; left: 26px; top: 130px;
    list-style: none;
    font-family: "Orbitron", sans-serif; font-weight: 500;
    font-size: 10px; letter-spacing: .06em;
    color: var(--ink);
  }
  .contact li { display: flex; align-items: center; gap: 7px; line-height: 17px; white-space: nowrap; }
  .contact__icon { width: 11px; height: 11px; flex: none; }

  .holder {
    position: absolute; right: 28px; bottom: 22px; text-align: right;
    font-family: "Orbitron", sans-serif; font-weight: 500; color: var(--ink);
    white-space: nowrap;
  }
  .holder__name { font-size: 14px; letter-spacing: .14em; text-transform: uppercase; }
  .holder__role { font-size: 9px; letter-spacing: .2em; text-transform: uppercase; margin-top: 3px; }
</style>
</head>
<body>
<main class="canvas">

  <section class="card card--front">
    <div class="brand"><span class="brand__dot"></span>Tarrow Building Ventures</div>
  </section>

  <section class="card card--back">
    <svg class="band" viewBox="0 0 540 309" width="540" height="309" aria-hidden="true">
      <defs>
        <linearGradient id="bandGradient" x1="0" y1="0" x2="1" y2="0">
          <stop offset="0" stop-color="var(--green-dark)"/>
          <stop offset="1" stop-color="var(--green-light)"/>
        </linearGradient>
      </defs>
      <path d="M0 104 C 150 99, 262 134, 342 178 S 482 218, 540 208 L540 309 L0 309 Z" fill="url(#bandGradient)"/>
      <path d="M0 88 C 150 82, 262 118, 342 164 S 482 204, 540 194 L540 198 C 482 209, 400 202, 338 172 S 150 97, 0 99 Z" fill="var(--ink)"/>
    </svg>

    <div class="brand"><span class="brand__dot"></span>Tarrow Building Ventures</div>

    <ul class="contact">
      <li>
        <svg class="contact__icon" viewBox="0 0 12 12"><circle cx="6" cy="6" r="6" fill="var(--ink)"/><path d="M6 2.5a2 2 0 0 0-2 2c0 1.6 2 4.5 2 4.5s2-2.9 2-4.5a2 2 0 0 0-2-2z" fill="#fff"/></svg>
        Unit 14, Reed Lane, VIC 3051
      </li>
      <li>
        <svg class="contact__icon" viewBox="0 0 12 12"><circle cx="6" cy="6" r="6" fill="var(--ink)"/><rect x="4" y="2.5" width="4" height="7" rx="1" fill="#fff"/></svg>
        03-5550-1842
      </li>
      <li>
        <svg class="contact__icon" viewBox="0 0 12 12"><circle cx="6" cy="6" r="6" fill="var(--ink)"/><rect x="4" y="2.5" width="4" height="7" rx="1" fill="#fff"/></svg>
        03-5550-2967
      </li>
      <li>
        <svg class="contact__icon" viewBox="0 0 12 12"><circle cx="6" cy="6" r="6" fill="var(--ink)"/><rect x="4" y="2.5" width="4" height="7" rx="1" fill="#fff"/></svg>
        04-5550-3318
      </li>
      <li>
        <svg class="contact__icon" viewBox="0 0 12 12"><circle cx="6" cy="6" r="6" fill="var(--ink)"/><rect x="3" y="4" width="6" height="4" fill="#fff"/><path d="M3 4l3 2.2L9 4" stroke="var(--ink)" stroke-width=".7" fill="none"/></svg>
        dale@tarrowbuild.test
      </li>
      <li>
        <svg class="contact__icon" viewBox="0 0 12 12"><circle cx="6" cy="6" r="6" fill="var(--ink)"/><circle cx="6" cy="6" r="3" stroke="#fff" stroke-width=".8" fill="none"/><path d="M3 6h6M6 3v6" stroke="#fff" stroke-width=".6"/></svg>
        www.tarrowbuild.test
      </li>
    </ul>

    <div class="holder">
      <div class="holder__name">Dale Harper</div>
      <div class="holder__role">Owner / C.E.O</div>
    </div>
  </section>

</main>
</body>
</html>
```